I will ask the design of the business card

We are looking for business card design of the new company "VORTELL PAYWORKS STUDIO LLC." Based in Azerbaijan.
In case
We are working on Azerbaijan to set up the first exchange of crypto currencies.

The key currency used in exchanges is called "MIRTA".
In case
We are doing project to make crypto currency infrastructure.

We provide state-of-the-art technology to the world.

```html
<!DOCTYPE html>
<html lang="en">
<head>
<meta charset="utf-8">
<title>Vortell Payworks Studio LLC. – Business Card</title>
<link rel="stylesheet" href="https://fonts.googleapis.com/css2?family=Poppins:wght@400;500;600;700&display=swap">
<style>
  :root {
    --stage: #1b1b1c;
    --card-light: #f4f5f6;
    --card-light-edge: #e4e6e8;
    --card-dark: #2c2c2e;
    --card-dark-tone: #3a3a3d;
    --brand-blue: #1f6fa8;
    --brand-sky: #2aa7dc;
    --ink: #3b3b3d;
    --ink-soft: #2a2a2c;
    --paper-white: #ffffff;
  }
  * { margin: 0; padding: 0; box-sizing: border-box; }
  html, body {
    width: 1200px; height: 900px; overflow: hidden;
    background: var(--stage);
    font-family: "Poppins", sans-serif;
  }
  .stage {
    position: relative; width: 1200px; height: 900px;
    display: flex; flex-direction: column; align-items: center; justify-content: center; gap: 44px;
  }
  .card {
    position: relative; width: 560px; height: 320px; border-radius: 22px; overflow: hidden;
  }
  /* Front */
  .card-front {
    background: linear-gradient(135deg, var(--paper-white) 0%, var(--card-light) 60%, var(--card-light-edge) 100%);
  }
  .person {
    position: absolute; left: 34px; top: 96px;
  }
  .person-name {
    color: var(--brand-blue); font-weight: 700; font-size: 17px; letter-spacing: 0.5px; text-transform: uppercase;
    line-height: 1.2;
  }
  .person-title {
    color: var(--ink-soft); font-weight: 500; font-size: 13.5px; line-height: 1.3;
  }
  .contact-list { list-style: none; margin-top: 12px; }
  .contact-item {
    display: flex; align-items: center; gap: 10px;
    color: var(--ink-soft); font-weight: 500; font-size: 12.5px; height: 24px;
  }
  .contact-icon { width: 16px; height: 16px; flex: none; }
  .divider {
    position: absolute; left: 212px; top: 137px; width: 300px; height: 2px; background: var(--brand-blue);
  }
  .brand {
    position: absolute; display: flex; align-items: center; gap: 10px;
  }
  .brand-mark { width: 14px; height: 14px; background: var(--brand-sky); flex: none; }
  .brand-name {
    font-weight: 600; font-size: 19px; letter-spacing: 0.6px; line-height: 1.15; text-transform: uppercase;
  }
  .card-front .brand { left: 254px; top: 56px; }
  .card-front .brand-name { color: var(--ink); }
  .address {
    position: absolute; right: 48px; top: 160px; text-align: right;
    color: var(--brand-blue); font-weight: 500; font-size: 13.5px; line-height: 1.45;
  }
  /* Back */
  .card-back { background: var(--card-dark); }
  .back-texture {
    position: absolute; inset: 0;
    background: radial-gradient(ellipse at 30% 35%, var(--card-dark-tone) 0%, var(--card-dark) 70%);
  }
  .card-back .brand { left: 50%; top: 50%; transform: translate(-50%, -50%); }
  .card-back .brand-name { color: var(--paper-white); font-size: 22px; }
</style>
</head>
<body>
<main class="stage">
  <section class="card card-front" aria-label="Business card front">
    <div class="brand">
      <span class="brand-mark"></span>
      <span class="brand-name">Vortell Payworks<br>Studio LLC.</span>
    </div>

    <div class="person">
      <p class="person-name">Leyla Rahimova</p>
      <p class="person-title">Chief Executive Officer</p>
      <ul class="contact-list">
        <li class="contact-item">
          <svg class="contact-icon" viewBox="0 0 16 16" aria-hidden="true">
            <circle cx="8" cy="8" r="8" fill="var(--brand-blue)"/>
            <path d="M5.2 4.2l1.4 1.6-.8 1c.5 1.1 1.3 1.9 2.4 2.4l1-.8 1.6 1.4-.9 1.4C7.6 11 5 8.4 4.8 5.1z" fill="#fff"/>
          </svg>
          123 555 047
        </li>
        <li class="contact-item">
          <svg class="contact-icon" viewBox="0 0 16 16" aria-hidden="true">
            <circle cx="8" cy="8" r="8" fill="var(--brand-blue)"/>
            <rect x="4" y="5.2" width="8" height="5.6" rx="0.6" fill="#fff"/>
            <path d="M4.3 5.6L8 8.4l3.7-2.8" fill="none" stroke="var(--brand-blue)" stroke-width="0.9"/>
          </svg>
          info@vortellpayworks.com
        </li>
        <li class="contact-item">
          <svg class="contact-icon" viewBox="0 0 16 16" aria-hidden="true">
            <circle cx="8" cy="8" r="8" fill="var(--brand-blue)"/>
            <path d="M7 9l2-2M6.4 7.6L5.3 8.7a1.4 1.4 0 002 2l1.1-1.1M9.6 8.4l1.1-1.1a1.4 1.4 0 00-2-2L7.6 6.4" fill="none" stroke="#fff" stroke-width="1.1" stroke-linecap="round"/>
          </svg>
          vortellpayworks.com
        </li>
      </ul>
    </div>

    <div class="divider"></div>

    <address class="address" style="font-style:normal">
      No.48 Nizami street<br>Baku AZ1010, Azerbaijan
    </address>
  </section>

  <section class="card card-back" aria-label="Business card back">
    <div class="back-texture" role="img" aria-label="Dark surface with a loose pattern of thin grey looping lines"></div>
    <div class="brand">
      <span class="brand-mark"></span>
      <span class="brand-name">Vortell Payworks<br>Studio LLC.</span>
    </div>
  </section>
</main>
</body>
</html>
```